Larkvale Advertising PowerPoint Design Project

We need PowerPoint slide templates for our Sales Media Kit at our re-branded company based in Canada called "Larkvale Advertising Network".

Looking for a look that clearly and powerfully portrays our unique and effective indoor advertising billboards in our network.

Our PetiPanels, GrandPanels and TitanFlags are strategically placed in high traffic areas of restaurants, pubs, nightclubs, fitness clubs, colleges and universities, and sports arenas.

Key features of our media is a captive audience and 100% gender specific.

You can visit our old website for info on the above three media products (plovercrest.ca)

Our Media Kits go out to small, medium business owners and advertising agenices.

Deliverables are:

1) Presentation cover slide with rich graphic content and space for content.
2) Presentation body slide with room for content 2 photos or logos. This slide should have the following:
a) No graphic in the text area
b) Space for page number at the bottom.
3) Photoshop (PSD) files for all graphic elements.
4) Font files for all fonts used.
Updates

Project Deadline Extended
Reason: Need more designs submitted.

We have uploaded our business card file.

Would like to incorporate the look, feel and colour of our business card to the power point template.

Target Market(s)

small business owners, marketing managers, media buyers and advertising agencies.

Industry/Entity Type

Advertising

Requirements
Must have
• We would like to see designs that:
- use the color scheme indicated by the attached logo design, perhaps expanding on it slightly.
- Look should be professional, smooth, and colourful.
-Must have a clean and modern feel that Ad Agencies would be impressed with.
-We have uploaded our business card file.

-Would like to incorporate the look, feel and colour of our business card to the power point template.

```html
<!DOCTYPE html>
<html lang="en">
<head>
<meta charset="utf-8">
<title>Larkvale Advertising Network – Slide Templates</title>
<link rel="stylesheet" href="https://fonts.googleapis.com/css2?family=Arimo:wght@400;700&display=swap">
<style>
  :root {
    --navy: #0c1a2e;
    --navy-deep: #08111f;
    --smoke: #2f5fa8;
    --accent: #3a7fd5;
    --ink: #555a60;
    --paper: #ffffff;
    --rule: #9fb3c8;
    --stage: #ffffff;
  }
  * { box-sizing: border-box; margin: 0; padding: 0; }
  html, body { width: 1200px; height: 348px; overflow: hidden; background: var(--stage); }
  body { position: relative; font-family: "Arimo", Arial, sans-serif; }

  .slide {
    position: absolute; top: 50px; height: 245px;
    background: var(--paper);
    box-shadow: 1px 2px 4px rgba(0,0,0,.35);
    overflow: hidden;
  }
  .slide--cover { left: 34px; width: 272px; background: var(--navy); }
  .slide--content { left: 433px; width: 329px; border: 1px solid #c8ccd2; }
  .slide--image { left: 823px; width: 329px; border: 1px solid #c8ccd2; }

  .smoke { position: absolute; inset: 0; }

  .cover-title {
    position: absolute; left: 166px; top: 133px;
    color: #fff; font-weight: 700; font-size: 11.5px; line-height: 14px;
    white-space: nowrap;
  }
  .cover-subtitle {
    position: absolute; left: 166px; top: 157px;
    color: var(--accent); font-size: 6.6px; line-height: 8px;
    white-space: nowrap;
  }
  .brand { position: absolute; display: flex; align-items: center; gap: 3px; }
  .brand__mark { width: 9px; height: 9px; background: var(--accent); }
  .brand__name { font-weight: 700; color: #cfd6df; }
  .brand--cover { left: 22px; top: 192px; }
  .brand--cover .brand__mark { width: 14px; height: 14px; }
  .brand--cover .brand__name { font-size: 14px; }
  .brand__tagline {
    position: absolute; left: 22px; top: 211px;
    font-size: 3.5px; color: #9aa6b5; letter-spacing: .3px; text-transform: uppercase;
  }

  .header {
    position: absolute; left: 0; top: 0; width: 100%; height: 30px;
    background: var(--navy);
  }
  .header .smoke { opacity: .9; }
  .header__title {
    position: absolute; left: 12px; top: 9px;
    color: #fff; font-weight: 700; font-size: 13.5px; letter-spacing: .3px;
    white-space: nowrap;
  }
  .brand--header { right: 10px; top: 10px; }
  .brand--header .brand__name { font-size: 10px; }

  .bullets {
    position: absolute; left: 14px; top: 37px;
    list-style: none; color: var(--ink); font-size: 9.6px; line-height: 11px;
  }
  .bullets li { position: relative; padding-left: 11px; margin-bottom: 4px; }
  .bullets li::before {
    content: "•"; position: absolute; left: 0; top: 0; color: var(--accent);
  }
  .bullets .sub { font-size: 8.4px; line-height: 9.6px; padding-left: 25px; }
  .bullets .sub::before { content: "–"; left: 13px; color: var(--ink); }
  .slide--content .bullets { width: 300px; }
  .slide--image .bullets { width: 162px; }

  .footer {
    position: absolute; left: 0; bottom: 0; width: 100%; height: 18px;
    border-top: 1px solid var(--rule);
    font-size: 5.5px; color: var(--accent);
  }
  .footer__date { position: absolute; left: 12px; top: 6px; }
  .footer__page { position: absolute; right: 14px; top: 6px; }

  .photo {
    position: absolute; left: 188px; top: 70px; width: 131px; height: 98px;
    border-radius: 12px;
    background: linear-gradient(160deg, #dbe9f6 0%, #7fa8cf 35%, #2f5c86 70%, #1c3550 100%);
  }
  .photo-reflection {
    position: absolute; left: 188px; top: 170px; width: 131px; height: 34px;
    border-radius: 0 0 12px 12px;
    background: linear-gradient(180deg, rgba(47,92,134,.35), rgba(255,255,255,0));
  }
</style>
</head>
<body>

<section class="slide slide--cover">
  <svg class="smoke" role="img" aria-label="Blue smoke wisps drifting over a dark navy background" viewBox="0 0 272 245" preserveAspectRatio="none">
    <defs>
      <radialGradient id="coverGlow" cx="30%" cy="45%" r="60%">
        <stop offset="0" stop-color="#2a5496" stop-opacity=".7"/>
        <stop offset="1" stop-color="#0c1a2e" stop-opacity="0"/>
      </radialGradient>
      <radialGradient id="coverGlow2" cx="80%" cy="15%" r="40%">
        <stop offset="0" stop-color="#2f5fa8" stop-opacity=".5"/>
        <stop offset="1" stop-color="#0c1a2e" stop-opacity="0"/>
      </radialGradient>
    </defs>
    <rect width="272" height="245" fill="url(#coverGlow)"/>
    <rect width="272" height="245" fill="url(#coverGlow2)"/>
  </svg>
  <h1 class="cover-title">Presentation Title</h1>
  <p class="cover-subtitle">Presentation subtitle and author</p>
  <div class="brand brand--cover"><span class="brand__mark"></span><span class="brand__name">Larkvale</span></div>
  <p class="brand__tagline">advertising network</p>
</section>

<section class="slide slide--content">
  <header class="header">
    <svg class="smoke" role="img" aria-label="Blue smoke texture across the title band" viewBox="0 0 329 30" preserveAspectRatio="none">
      <defs>
        <linearGradient id="bandSmoke" x1="0" x2="1">
          <stop offset="0" stop-color="#2f5fa8" stop-opacity=".2"/>
          <stop offset=".35" stop-color="#3c6fbf" stop-opacity=".7"/>
          <stop offset=".7" stop-color="#1d3a6a" stop-opacity=".3"/>
          <stop offset="1" stop-color="#2f5fa8" stop-opacity=".5"/>
        </linearGradient>
      </defs>
      <rect width="329" height="30" fill="url(#bandSmoke)"/>
    </svg>
    <h2 class="header__title">Content Slide Title</h2>
    <div class="brand brand--header"><span class="brand__mark"></span><span class="brand__name">Larkvale</span></div>
  </header>
  <ul class="bullets">
    <li>Lorem ipsum dolor sit amet, consectetur adipiscing elit. Vestibulum leo elit, vehicula eu tempus vel, posuere ac nisi.</li>
    <li>Class aptent taciti sociosqu ad litora torquent per conubia nostra, per inceptos himenaeos.</li>
    <li>Integer leo arcu, lacinia id lacinia sit amet, egestas sed lectus.</li>
    <li class="sub">Donec ut purus et enim pretium commodo sed id magna. Class aptent taciti sociosqu ad litora torquent per conubia nostra, per inceptos himenaeos.</li>
    <li class="sub">Nullam felis ipsum, fermentum vitae sagittis id, semper sit amet felis. Quisque luctus sollicitudin libero, sit amet sodales enim scelerisque pulvinar.</li>
    <li>Class aptent taciti sociosqu ad litora torquent per conubia nostra, per inceptos himenaeos.</li>
    <li>Duis fermentum neque et nisl tincidunt scelerisque.</li>
  </ul>
  <footer class="footer"><span class="footer__date">28-09-2012</span><span class="footer__page">2</span></footer>
</section>

<section class="slide slide--image">
  <header class="header">
    <svg class="smoke" role="img" aria-label="Blue smoke texture across the title band" viewBox="0 0 329 30" preserveAspectRatio="none">
      <rect width="329" height="30" fill="url(#bandSmoke)"/>
    </svg>
    <h2 class="header__title">Content and Image Slide Title</h2>
    <div class="brand brand--header"><span class="brand__mark"></span><span class="brand__name">Larkvale</span></div>
  </header>
  <ul class="bullets">
    <li>Lorem ipsum dolor sit amet, consectetur adipiscing elit. Vestibulum leo elit, vehicula eu tempus vel, posuere ac nisi.</li>
    <li>Class aptent taciti sociosqu ad litora torquent per conubia nostra, per inceptos himenaeos.</li>
    <li>Integer leo arcu, lacinia id lacinia sit amet, egestas sed lectus.</li>
    <li class="sub">Donec ut purus et enim pretium commodo sed id magna. Class aptent taciti sociosqu ad litora torquent per conubia nostra, per inceptos himenaeos.</li>
    <li>Duis fermentum neque et nisl tincidunt scelerisque.</li>
  </ul>
  <div class="photo" role="img" aria-label="Photo of glass office towers rising into a blue sky"></div>
  <div class="photo-reflection"></div>
  <footer class="footer"><span class="footer__date">28-09-2012</span><span class="footer__page">3</span></footer>
</section>

</body>
</html>
```